NORELO - Webdesign für eine Poolreinigungsfirma
Zielgruppe
Wir sind NORELO, eine junge Poolreinigungsfirma die gerade erst in den Startlöchern sitzt. Wir befinden uns auf der französischen Insel LA RÉUNION und richten uns an Personen jeglichen Alters, die einen Pool besitzen.
Aufgabenstellung
Wir wünschen uns ein in erster Linie LUXURIÖSES, schickes und sehr ansprechendes Webdesign, dass - unbedingt - die Verbindung zur Natur zeigt (Tropen, Beispielfotos im Anhang). Natur + Wasser / Pool.
BITTE KEINE TYPISCHE POOLWEBSITE, da wir u.a. auch bald in den Verkauf luxuriöser Accessoires gehen möchten. Wir möchten uns von der Konkurrenz stark und deutlich abheben.
Wir wünschen uns einen DUNKLEN MOOD (gerne auch schwarz auf weißem Hintergrund o.ä. ?).
Wir sind von AI-Bildern sehr angetan, da sie Träume erwecken und in der Tiefe ansprechen können. Nutzen Sie diese gerne, bieten Sie uns Vorschläge. Bitte passend zu den Tropen.
Wir überlassen Ihnen vertrauensvoll die Erstellung des Designs der Website (Aufbau, etc), wir möchten uns überraschen lassen.
Unser Logo, ein Briefing für drei gewünschte Seiten und Beispielbilder, die sehr gerne genutzt werden können (oder in Anlehnung an diese, gleicher Stil) sind im Anhang zu finden.
Die Seite sollte unbedingt - auch - die Nutzung mit Mobiltelefonen ermöglichen und keine Verzögerungen beim Aufrufen / Laden der Website aufzeigen.

```html
<!DOCTYPE html>
<html lang="fr">
<head>
<meta charset="utf-8">
<title>NORELO – Entretien et nettoyage piscine</title>
<link rel="stylesheet" href="https://fonts.googleapis.com/css2?family=Alata&family=Playfair+Display:wght@900&display=swap">
<style>
  :root {
    --bg: #000000;
    --text: #ffffff;
    --brand-ink: #33444d;
    --brand-mark: #2aa59c;
    --photo-thatch: #b09678;
    --photo-thatch-dark: #7d6a55;
    --photo-leaf: #3c4a2c;
    --photo-shade: #1a2619;
    --photo-wall: #cfc9bd;
  }
  * { margin: 0; padding: 0; box-sizing: border-box; }
  html, body {
    width: 1200px; height: 758px; overflow: hidden;
    background: var(--bg); color: var(--text);
  }
  .page { position: relative; width: 1200px; height: 758px; overflow: hidden; }
  .section-title {
    font-family: "Playfair Display", serif;
    font-weight: 900;
    font-size: 41px;
    line-height: 53px;
    letter-spacing: -0.6px;
    text-transform: uppercase;
    white-space: nowrap;
  }
  .section-text {
    font-family: "Alata", sans-serif;
    font-size: 13.5px;
    line-height: 28.5px;
    white-space: nowrap;
  }
  .intro { position: absolute; left: 137px; top: 58px; width: 620px; }
  .intro .section-text { margin-top: 24px; }
  .experiences { position: absolute; left: 752px; top: 626px; width: 440px; }
  .experiences .section-text { margin-top: 20px; }
  .brand {
    position: absolute; left: 917px; top: 68px; width: 154px;
    display: flex; flex-direction: column; align-items: center; gap: 20px;
  }
  .brand-mark {
    width: 72px; height: 72px; border-radius: 50%;
    background: var(--brand-mark);
  }
  .brand-name {
    font-family: "Alata", sans-serif;
    font-size: 31px; line-height: 1;
    letter-spacing: 5px;
    color: var(--brand-ink);
  }
  .hero-photo { position: absolute; left: 0; top: 0; }
</style>
</head>
<body>
<main class="page">
  <section class="intro">
    <h1 class="section-title">Entretien et nettoyage<br>piscine</h1>
    <p class="section-text">Parce que l’entretien et le nettoyage d’une piscine nécessitent de réelles connaissances,<br>choisir un contrat d’entretien de NORELO c’est la certitude d’un service haut de gamme :</p>
  </section>

  <div class="brand">
    <span class="brand-mark"></span>
    <span class="brand-name">NORELO</span>
  </div>

  <svg class="hero-photo" width="1200" height="758" viewBox="0 0 1200 758" role="img" aria-label="Photo de paillotes au toit de chaume entourées de palmiers tropicaux">
    <defs>
      <linearGradient id="photoBase" x1="0" y1="0" x2="1" y2="0">
        <stop offset="0" stop-color="var(--photo-leaf)"/>
        <stop offset="0.3" stop-color="var(--photo-thatch-dark)"/>
        <stop offset="0.6" stop-color="var(--photo-thatch)"/>
        <stop offset="1" stop-color="var(--photo-thatch-dark)"/>
      </linearGradient>
      <radialGradient id="photoShade" cx="0.35" cy="0.85" r="0.55">
        <stop offset="0" stop-color="var(--photo-wall)" stop-opacity="0.35"/>
        <stop offset="1" stop-color="var(--photo-shade)" stop-opacity="0"/>
      </radialGradient>
      <linearGradient id="photoEdge" x1="0" y1="0" x2="1" y2="0">
        <stop offset="0" stop-color="var(--photo-shade)" stop-opacity="0.7"/>
        <stop offset="0.25" stop-color="var(--photo-shade)" stop-opacity="0"/>
      </linearGradient>
      <clipPath id="photoShape">
        <path d="M0 508 C90 500 170 520 260 514 C340 508 400 478 465 485 C535 494 572 560 575 640 C577 690 573 730 571 758 L0 758 Z"/>
      </clipPath>
    </defs>
    <g clip-path="url(#photoShape)">
      <rect x="0" y="470" width="600" height="288" fill="url(#photoBase)"/>
      <rect x="0" y="470" width="600" height="288" fill="url(#photoShade)"/>
      <rect x="0" y="470" width="600" height="288" fill="url(#photoEdge)"/>
    </g>
  </svg>

  <section class="experiences">
    <h2 class="section-title">Expériences</h2>
    <p class="section-text">Riche d’une expérience de 20 ans, nous nous adressons<br>aux particuliers, professionnels, location saisonnière et bien plus.</p>
  </section>
</main>
</body>
</html>
```